Business Card for Musician

The company is called Tolvik Music Entertainment and i am the director (Priya Hallorin) . I would like a logo made along with a list of services i provide :

Rock Pop and Jazz Covers music for Weddings , Birthdays , Pubs, Bars and Restaurants

I provide Solo/Duo and Bands for these functions.

Another aspect is i teach guitar and do music workshops and compose music for television.

I want to go for something different than a photo of a guitar or singer..i like the idea of soundwaves and an ear. or ripples of sound like a music note (as a drop of water) and the sound rippling out..another idea is something with lighting (music lights) with different colours lighting up the name Tolvik..however im open to any ideas. Thanks

Target Market(s)

General Public, Music Agents, Venue Owners. English Speaking..adults from 25-50

Industry/Entity Type

Business

Font styles to use
Sans Serif

Colors

Designer to choose colors to be used in the design.

Requirements
Must have
• All the points about what i do...
Nice to have
• Logo could emphasize the TOL in Tolvik...
Should not have
• Not too busy please...Simple but gets the message across. NOthing obvious like a photo of a musician playing.

```html
<!DOCTYPE html>
<html lang="en">
<head>
<meta charset="utf-8">
<title>Tolvik Music Entertainment — Business Card</title>
<link rel="stylesheet" href="https://fonts.googleapis.com/css2?family=Open+Sans:wght@400;600&display=swap">
<style>
  :root {
    --backdrop: #d9d9d7;
    --card: #1e1e1e;
    --arc: #080808;
    --text: #e6e6e6;
    --accent: #1b9ad6;
  }
  html, body {
    margin: 0;
    width: 1200px;
    height: 1000px;
    overflow: hidden;
    background: var(--backdrop);
    font-family: "Open Sans", sans-serif;
  }
  .card {
    position: absolute;
    left: 100px;
    top: 214px;
    width: 1000px;
    height: 571px;
    background: var(--card);
    overflow: hidden;
    color: var(--text);
  }
  .card-arcs {
    position: absolute;
    inset: 0;
  }
  .brand {
    position: absolute;
    left: 40px;
    top: 40px;
    display: flex;
    align-items: center;
    gap: 22px;
  }
  .brand-dot {
    width: 52px;
    height: 52px;
    border-radius: 50%;
    border: 3px solid var(--accent);
    box-sizing: border-box;
  }
  .brand-name {
    font-weight: 600;
    font-size: 27px;
    line-height: 1.05;
    text-transform: uppercase;
    color: #ffffff;
  }
  .contact {
    position: absolute;
    left: 690px;
    top: 165px;
    font-size: 22px;
    line-height: 1.15;
  }
  .contact-name { color: var(--accent); }
  .service {
    position: absolute;
    font-size: 22px;
    white-space: nowrap;
    letter-spacing: 0.2px;
  }
</style>
</head>
<body>
  <section class="card" aria-label="Tolvik Music Entertainment business card">
    <svg class="card-arcs" width="1000" height="571" viewBox="0 0 1000 571" aria-hidden="true">
      <circle cx="66" cy="66" r="620" fill="none" stroke="var(--arc)" stroke-width="2"/>
      <circle cx="66" cy="66" r="900" fill="none" stroke="var(--arc)" stroke-width="2"/>
    </svg>

    <div class="brand">
      <span class="brand-dot"></span>
      <div class="brand-name">Tolvik Music<br>Entertainment</div>
    </div>

    <div class="contact">
      <div class="contact-name">Priya Hallorin</div>
      <div class="contact-role">Director</div>
    </div>

    <div class="service" style="left:480px; top:232px;">Solo/Duo/Band</div>
    <div class="service" style="left:455px; top:292px;">Pop/Rock/Jazz</div>
    <div class="service" style="left:450px; top:352px;">Cover Music</div>
    <div class="service" style="left:385px; top:412px;">Weddings/Birthdays</div>
    <div class="service" style="left:340px; top:472px;">Restaurants/Bars/Pubs</div>

    <div class="service" style="left:640px; top:332px;">Guitar Tutoring</div>
    <div class="service" style="left:630px; top:392px;">Music Workshop</div>
    <div class="service" style="left:620px; top:452px;">Music for Television</div>
  </section>
</body>
</html>
```